Business Card Design

I would like a double sided business card design.

1 side showing usual contact details and small version of logo (attached "GlanMare")

other side with larger logo and artwork with room to list what we specialise in.

Glan Mare is a Fashion Millinery Design and Sales Business.

I have attached some other examples of te styles i like so you can see what sort of taste i have.

Feel free to play around with colours of logo - it is grey as i originall had in mind a black background with monochrome silver logo.
Updates

• Please send me a message with your quote after posting your design. Budget set at Minimum (FYI) and negotiable
• Supporting files are examples only - i do not wish to copy them.  The only file for exact use is my logo "GlanMare"
• Thank you

Target Market(s)

18 - 80 yo females mainly

Industry/Entity Type

Business

Requirements
Must have
• unique and striking individuality
Should not have
• boring and normal

```html
<!DOCTYPE html>
<html lang="en">
<head>
<meta charset="utf-8">
<title>GlanMare — Business Card</title>
<link rel="stylesheet" href="https://fonts.googleapis.com/css2?family=Roboto+Condensed:wght@300;400;700&display=swap">
<style>
  :root {
    --page: #ffffff;
    --card-center: #ffffff;
    --card-edge: #ececec;
    --pink: #f29cbf;
    --pink-soft: #f6c3d8;
    --ink: #231f20;
    --slate: #3f4346;
  }
  * { box-sizing: border-box; margin: 0; padding: 0; }
  html, body {
    width: 1200px; height: 904px; overflow: hidden;
    background: var(--page);
    font-family: "Roboto Condensed", "Arial Narrow", sans-serif;
  }
  .sheet { position: relative; width: 1200px; height: 904px; }
  .card {
    position: absolute; top: 140px;
    width: 514px; height: 307px; overflow: hidden;
    background: radial-gradient(ellipse at 45% 55%, var(--card-center) 0%, var(--card-edge) 100%);
  }
  .card--front { left: 69px; }
  .card--back  { left: 624px; }

  .ornament { position: absolute; background: var(--pink); }
  .ornament--corner {
    left: 0; top: 0; width: 142px; height: 113px;
    border-radius: 0 0 100% 0;
  }
  .ornament--scroll {
    right: 0; bottom: 0; width: 284px; height: 142px;
    border-radius: 100% 0 0 0;
  }
  .brushwork {
    position: absolute; left: 0; top: 0; width: 77px; height: 269px;
    background: linear-gradient(to bottom, var(--pink) 0%, var(--pink-soft) 55%, rgba(246,195,216,0) 100%);
  }

  .wordmark {
    position: absolute; font-weight: 300; color: var(--slate);
    line-height: 1; white-space: nowrap; letter-spacing: -0.5px;
  }
  .card--front .wordmark { left: 125px; top: 116px; font-size: 64px; }
  .card--back .wordmark { left: 144px; top: 90px; font-size: 60px; color: var(--ink); }

  .contact {
    position: absolute; left: 0; right: 0; top: 155px;
    padding-left: 100px; text-align: center;
    color: var(--ink); font-size: 15px; line-height: 18px;
  }
  .contact b { font-weight: 700; }

  .fields { position: absolute; left: 0; top: 275px; width: 100%; height: 30px; }
  .field {
    position: absolute; top: 0; height: 29px;
    border-left: 1px solid var(--ink);
    padding-left: 5px; font-size: 14px; line-height: 16px; color: var(--ink);
  }
  .field--name  { left: 17px; }
  .field--cell  { left: 135px; }
  .field--email { left: 258px; }
</style>
</head>
<body>
<main class="sheet">
  <section class="card card--front" aria-label="Card front">
    <div class="ornament ornament--corner" role="img" aria-label="Pink floral scroll ornament in the top-left corner"></div>
    <div class="ornament ornament--scroll" role="img" aria-label="Large pink swirling floral scroll ornament in the bottom-right corner"></div>
    <h1 class="wordmark">GlanMare</h1>
  </section>

  <section class="card card--back" aria-label="Card back">
    <div class="brushwork" role="img" aria-label="Pink vertical brush strokes fading downwards"></div>
    <h2 class="wordmark">GlanMare</h2>
    <address class="contact" style="font-style:normal">
      <p>Abcd, efghijklmnopqrst, vwxyz</p>
      <p><b>Ph:</b> 91+00000000000, 000000</p>
      <p><b>Email:</b> hello@glanmare.com</p>
      <p><b>Website:</b> www.glanmare.com</p>
    </address>
    <div class="fields">
      <span class="field field--name">director Name</span>
      <span class="field field--cell">cell</span>
      <span class="field field--email">email</span>
    </div>
  </section>
</main>
</body>
</html>
```